Business Card Design for Portrait photography professional

We are a small company specializing in portrait photography (weddings, family, couples, children, newborn, pregnant, etc.) Occasionally we do business portraits too and do some other type of photography. We need a business card which would fit into the same look and feel as our website theme (lumvika.com - under construction currently).
Our target customer base lies within mid- to upmarket. We want our business cards to convey a feeling of quality, solidness and a bit luxury.
Design should be universal and usable on 85mmx55mm, 90mmx50mm and 90mmx55mm
one extra file (PSD of a website didn't fit into the allowed updoad, therefore has put it into my filecrate: https://www.filecrate-example.net/s/qt7wk2rbvx9dmhe/website%20theme%20PSD.psd)

Target Market(s)

mostly private people, 25-60 years old, mostly well established.

Industry/Entity Type

Portrait Photography

Requirements
Must have
• 2 sided design (print on both sides of the business card).
Must include:
business name, logo, URL (lumvika.no) , employee name, email address, and phone number.
Colorscheme of the website lumvika.no / lumvika.com

```html
<!DOCTYPE html>
<html lang="en">
<head>
<meta charset="utf-8">
<title>Lumvika — Business Card</title>
<link rel="stylesheet" href="https://fonts.googleapis.com/css2?family=Crimson+Text:wght@400&display=swap">
<style>
  :root {
    --backdrop: #1c1c1c;
    --card: #141414;
    --card-edge: #232323;
    --ink: #e9e9e9;
    --ink-soft: #b9b9b9;
    --rule: #8a8a8a;
  }
  * { margin: 0; padding: 0; box-sizing: border-box; }
  html, body {
    width: 1200px; height: 900px; overflow: hidden;
    background: var(--backdrop);
    font-family: "Crimson Text", "Times New Roman", serif;
    color: var(--ink);
  }
  .stage {
    width: 1200px; height: 900px;
    display: flex; align-items: center; justify-content: center; gap: 80px;
  }
  .card {
    width: 360px; height: 556px;
    border-radius: 26px;
    background: linear-gradient(160deg, var(--card-edge), var(--card) 60%);
    box-shadow: 0 18px 40px rgba(0,0,0,.55);
    display: flex; flex-direction: column; align-items: center;
    text-align: center;
  }
  .card--front { justify-content: center; }
  .brand {
    display: flex; align-items: center; gap: 14px;
  }
  .brand__dot {
    width: 22px; height: 22px; border-radius: 50%;
    border: 2px solid var(--ink);
  }
  .brand__name {
    font-size: 44px; letter-spacing: 3px; color: var(--ink);
  }
  .card--back { padding-top: 64px; }
  .card--back .brand__name { font-size: 32px; letter-spacing: 2px; }
  .card--back .brand__dot { width: 16px; height: 16px; }
  .person { margin-top: 70px; }
  .person__name { font-size: 26px; letter-spacing: .5px; }
  .person__role { font-size: 15px; color: var(--ink-soft); margin-top: 2px; }
  .contact { margin-top: 44px; width: 200px; }
  .contact__item { padding: 8px 0 9px; }
  .contact__item + .contact__item { border-top: 1px solid var(--rule); }
  .contact__label { font-size: 14px; color: var(--ink-soft); }
  .contact__value { font-size: 19px; letter-spacing: .5px; }
</style>
</head>
<body>
<main class="stage">
  <section class="card card--front" aria-label="Card front">
    <div class="brand">
      <span class="brand__dot"></span>
      <span class="brand__name">Lumvika</span>
    </div>
  </section>

  <section class="card card--back" aria-label="Card back">
    <div class="brand">
      <span class="brand__dot"></span>
      <span class="brand__name">Lumvika</span>
    </div>
    <div class="person">
      <p class="person__name">Torben Vallinger</p>
      <p class="person__role">Managing Director</p>
    </div>
    <div class="contact">
      <div class="contact__item">
        <p class="contact__label">Phone</p>
        <p class="contact__value">4100 237 519</p>
      </div>
      <div class="contact__item">
        <p class="contact__label">Email</p>
        <p class="contact__value">info@lumvika.no</p>
      </div>
      <div class="contact__item">
        <p class="contact__label">Web</p>
        <p class="contact__value">www.lumvika.no</p>
      </div>
    </div>
  </section>
</main>
</body>
</html>
```